Public Assistance Direct mail piece

need a full color 2 sided marketing brochure to use in direct mail campaign. finished product will be printed on 2 times. initially full color brochures to be printed in bulk. Then consumer contact info and case manager contact info will be added at a later date.
brochure will need to have 2 blank areas on front side to print address that will show thru window envelope and sales agent info on for mail campaign.
Would like to see designs that include our current color scheme and logo.
Target market. Low income poverty. Non profit service offering free assistance to help low income seniors get free assitance thru state and federal public assistance programs.
1. Tovalink - over 1 in 5 recieve help from state Tovalink. Tovalink programs for seniors and persons on Sunbrook can pay doctor copays, deductibles, and assist with medical bills.
2. Brightway Program - receive Federal assistance with prescription medications, deductibles, copays, and drug plan premiums.
3. Sunbrook Savings Program - many adults 65 and over are eligible to receive Sunbrook at no cost. The program will pay your Sunbrook Part B premium and can even refund some previous payments.

You may be eligible to participate in one or more of these programs. All programs are based on limited income and assets.

To learn more call your local county case manager.

Knowledge is Power. Lets up help empower you.
Pay it forward. Who else do you know that is on Sunbrook that could use some help?

many graphs and illustrations are available form each government agency.

Target Market(s)

Seniors 65 plus, Sunbrook recipients

Industry/Entity Type

Marketing

Colors
0355a3
ec1f27
ffffff

Requirements
Must have
• logo, non profit, will need a government disclaimer somewhere
Nice to have
• photos of seniors saving money.

```html
<!DOCTYPE html>
<html lang="en">
<head>
<meta charset="utf-8">
<title>Elderway Aid Network – Direct Mail Brochure</title>
<link rel="stylesheet" href="https://fonts.googleapis.com/css2?family=Arimo:wght@400;700&family=Open+Sans:ital,wght@0,300;0,400;1,400&family=Tinos:wght@400;700&display=swap">
<style>
  :root{
    --navy:#1b3a66;
    --royal:#0355a3;
    --red:#ec1f27;
    --white:#ffffff;
    --sky:#b9def3;
    --sky-pale:#dceff9;
    --ink:#3c4a5c;
    --grey:#8a94a0;
    --orange:#f08a4b;
    --stage:#dde1ea;
  }
  *{margin:0;padding:0;box-sizing:border-box}
  html,body{width:1200px;height:1200px;overflow:hidden}
  body{background:var(--stage);position:relative;font-family:"Open Sans",Arial,sans-serif}

  .spread{position:absolute;left:246px;width:708px;height:550px;overflow:hidden;background:var(--white)}
  .spread--outside{top:40px}
  .spread--inside{top:610px}
  .spread__art{position:absolute;inset:0;width:708px;height:550px}
  .abs{position:absolute}

  /* outside: mailing panel */
  .mail-box{position:absolute;border:3px solid #111;background:var(--white);display:flex;align-items:center;justify-content:center}
  .mail-box--consumer{left:30px;top:22px;width:296px;height:222px}
  .mail-box--agent{left:28px;top:296px;width:137px;height:195px}
  .mail-box__label{writing-mode:vertical-rl;font-family:"Arimo",sans-serif;font-size:10px;color:#111;text-align:center;line-height:1.3}
  .mail-tagline{left:78px;top:257px;width:200px;text-align:center;font-size:11px;font-weight:300;color:var(--grey);line-height:1.35}
  .mail-contact{left:16px;font-family:"Tinos",serif;font-weight:700;font-size:12px;color:#222;display:flex;align-items:center;gap:6px}
  .mail-contact--phone{top:498px}
  .mail-contact--web{top:517px}
  .mail-contact svg{width:12px;height:12px}
  .return-address{left:250px;top:492px;width:80px;text-align:center;font-family:"Tinos",serif;font-size:5.5px;line-height:1.5;color:#222}
  .return-address__mark{display:block;width:7px;height:7px;background:var(--red);margin:0 auto 2px}
  .disclaimer{left:334px;top:130px;height:290px;writing-mode:vertical-rl;transform:rotate(180deg);font-family:"Tinos",serif;font-size:6.5px;color:#222;text-align:center}

  /* outside: cover panel */
  .brand{left:365px;top:32px;display:flex;align-items:flex-start;gap:6px}
  .brand__dot{width:14px;height:14px;border-radius:50%;background:var(--red);margin-top:4px}
  .brand__name{font-family:"Arimo",sans-serif;font-weight:700;font-size:14px;line-height:1.05;color:var(--navy);text-transform:uppercase;letter-spacing:.3px}
  .brand__tag{font-family:"Arimo",sans-serif;font-weight:700;font-size:6px;color:var(--navy);text-transform:uppercase;margin-top:4px;letter-spacing:.2px}
  .cover-title{left:460px;top:218px;width:256px;text-align:center;font-family:"Arimo",sans-serif;font-weight:400;font-size:20.5px;line-height:1.22;color:var(--navy)}
  .cover-title em{font-style:normal;color:var(--red)}
  .cover-caption{left:350px;top:521px;width:358px;text-align:center;font-family:"Arimo",sans-serif;font-weight:700;font-size:7.5px;color:var(--white)}

  /* inside */
  .section-title{font-family:"Open Sans",sans-serif;font-weight:400;font-size:14px;white-space:nowrap}
  .bullets{list-style:none;font-size:9.5px;font-weight:300;line-height:1.3}
  .bullets li{position:relative;padding-left:17px;margin-bottom:10px}
  .bullets li::before{content:"";position:absolute;left:0;top:3px;width:8px;height:8px;border-radius:50%;background:var(--dot)}
  .program--tovalink{left:40px;top:78px;width:240px;color:var(--ink);--dot:#79c3ea}
  .program--tovalink .section-title{color:var(--navy);margin-bottom:8px}
  .program--savings{left:409px;top:28px;width:290px;color:#d7e3f0;--dot:#cfe4f5}
  .program--savings .section-title{color:var(--white);margin-bottom:38px;padding-left:83px}
  .program--savings .bullets{width:240px}
  .program--brightway{left:450px;top:316px;width:240px;color:var(--ink);--dot:var(--navy)}
  .program--brightway .section-title{color:var(--red);margin-bottom:16px;padding-left:97px}
  .eligible{left:255px;top:214px;width:188px;text-align:center;font-style:italic;font-size:15px;line-height:1.27;color:var(--orange)}
  .eligible small{display:block;font-size:9px;line-height:1.9}
  .pay-forward{left:312px;top:415px;width:396px;text-align:center;font-family:"Arimo",sans-serif;font-style:italic;font-size:15px;line-height:1.3;color:var(--navy)}
  .call-cta{left:316px;top:478px;font-family:"Tinos",serif;font-weight:700;color:var(--red);font-size:15px;line-height:1.2}
  .call-cta small{font-size:9px}
  .contact-note{left:522px;top:474px;width:154px;height:56px;background:#f1ece8;border-radius:0 0 0 12px;box-shadow:2px 2px 3px rgba(0,0,0,.18);display:flex;align-items:center;justify-content:center;text-align:center;font-style:italic;font-size:9.5px;line-height:1.3;color:var(--orange)}
  .pie-label{left:128px;top:248px;width:30px;text-align:center;font-family:"Arimo",sans-serif;font-weight:700;font-size:7px;color:var(--white)}
</style>
</head>
<body>

<!-- OUTSIDE SPREAD -->
<section class="spread spread--outside" aria-label="Brochure outside">
  <svg class="spread__art" viewBox="0 0 708 550">
    <defs>
      <linearGradient id="coverPaper" x1="0" y1="0" x2="1" y2="1">
        <stop offset="0" stop-color="#ffffff"/><stop offset="1" stop-color="#dfe3e8"/>
      </linearGradient>
      <linearGradient id="coverPhoto" x1="0" y1="0" x2="1" y2="1">
        <stop offset="0" stop-color="#3e5878"/><stop offset=".55" stop-color="#7f8fa3"/><stop offset="1" stop-color="#2a3b55"/>
      </linearGradient>
    </defs>
    <rect x="0" y="0" width="350" height="550" fill="var(--navy)"/>
    <rect x="15" y="16" width="330" height="519" fill="var(--white)"/>
    <rect x="350" y="0" width="358" height="550" fill="url(#coverPaper)"/>
    <polygon points="445,0 708,0 708,90 595,150" fill="var(--navy)"/>
    <polygon points="350,295 708,95 708,550 350,550" fill="var(--sky)"/>
    <line x1="350" y1="295" x2="708" y2="95" stroke="var(--navy)" stroke-width="3"/>
    <line x1="580" y1="167" x2="620" y2="144" stroke="var(--red)" stroke-width="3"/>
    <circle cx="595" cy="150" r="17" fill="var(--red)"/>
    <path d="M350,405 C440,350 600,330 708,340 L708,550 L350,550 Z" fill="var(--white)" opacity=".85"/>
    <g role="img" aria-label="Photo: senior hands placing a coin into a piggy bank">
      <path d="M350,428 C450,360 600,352 708,350 L708,550 L350,550 Z" fill="url(#coverPhoto)"/>
    </g>
    <path d="M350,428 C450,360 600,352 708,350" fill="none" stroke="var(--royal)" stroke-width="6"/>
    <rect x="346" y="0" width="8" height="550" fill="#000" opacity=".05"/>
  </svg>

  <div class="mail-box mail-box--consumer"><span class="mail-box__label">consumer contact info</span></div>
  <p class="abs mail-tagline">Knowledge is Power. Lets up help empower you</p>
  <div class="mail-box mail-box--agent"><span class="mail-box__label">case manager<br>contact info</span></div>

  <p class="abs mail-contact mail-contact--phone">
    <svg viewBox="0 0 24 24"><path fill="var(--red)" d="M6.6 10.8a15 15 0 0 0 6.6 6.6l2.2-2.2a1 1 0 0 1 1-.25 11.4 11.4 0 0 0 3.6.6 1 1 0 0 1 1 1V20a1 1 0 0 1-1 1A17 17 0 0 1 3 4a1 1 0 0 1 1-1h3.5a1 1 0 0 1 1 1c0 1.25.2 2.45.6 3.6a1 1 0 0 1-.25 1z"/></svg>
    800-555-0142 (toll free)
  </p>
  <p class="abs mail-contact mail-contact--web">
    <svg viewBox="0 0 24 24"><circle cx="12" cy="12" r="10" fill="none" stroke="var(--red)" stroke-width="2.4"/><path d="M2 12h20M12 2v20" stroke="var(--red)" stroke-width="2"/></svg>
    www.elderwayaid.org
  </p>
  <p class="abs return-address"><span class="return-address__mark"></span>Elderway Aid Network<br>PO Box 4470<br>Maple Ford, OH 43012</p>
  <p class="abs disclaimer">Not connected with or endorsed by the US Government or the Federal Sunbrook Program</p>

  <div class="abs brand">
    <span class="brand__dot"></span>
    <div>
      <p class="brand__name">Elderway<br>Aid<br>Network</p>
      <p class="brand__tag">Life, Health and Wealth Protection</p>
    </div>
  </div>
  <h1 class="abs cover-title">Non Profit Service<br>Offering Free<br>Assistance to<br><em>Low Income</em> Seniors</h1>
  <p class="abs cover-caption">"Helping seniors with their Life, Health and Wealth Protection"</p>
</section>

<!-- INSIDE SPREAD -->
<section class="spread spread--inside" aria-label="Brochure inside">
  <svg class="spread__art" viewBox="0 0 708 550">
    <defs>
      <linearGradient id="wash" x1="0" y1="0" x2="1" y2="1">
        <stop offset="0" stop-color="#cfe6f4"/><stop offset=".5" stop-color="#f4f9fc"/><stop offset="1" stop-color="#d6ecf7"/>
      </linearGradient>
      <linearGradient id="teamPhoto" x1="0" y1="0" x2="1" y2="1">
        <stop offset="0" stop-color="#1f3c68"/><stop offset="1" stop-color="#2b4d7e"/>
      </linearGradient>
      <linearGradient id="familyPhoto" x1="0" y1="0" x2="1" y2="1">
        <stop offset="0" stop-color="#c9a98f"/><stop offset=".5" stop-color="#efe2d6"/><stop offset="1" stop-color="#b58a6c"/>
      </linearGradient>
    </defs>
    <rect width="708" height="550" fill="var(--sky)"/>
    <rect width="360" height="400" fill="url(#wash)"/>
    <polygon points="310,385 480,300 708,225 708,550 310,550" fill="var(--sky)"/>
    <g role="img" aria-label="Photo: senior couple meeting with an advisor, navy tinted">
      <polygon points="185,0 708,0 708,225 480,300" fill="url(#teamPhoto)"/>
    </g>
    <line x1="185" y1="0" x2="462" y2="282" stroke="var(--navy)" stroke-width="3"/>
    <line x1="310" y1="385" x2="450" y2="315" stroke="var(--navy)" stroke-width="3"/>
    <line x1="505" y1="290" x2="708" y2="223" stroke="var(--red)" stroke-width="3"/>
    <circle cx="173" cy="285" r="56" fill="#9fd3f0"/>
    <path d="M173,285 L117,285 A56,56 0 0 1 173,229 Z" fill="var(--navy)"/>
    <circle cx="480" cy="300" r="34" fill="var(--red)"/>
    <circle cx="480" cy="300" r="26" fill="var(--white)"/>
    <path d="M480,274 V326 M454,300 H506" stroke="var(--red)" stroke-width="4"/>
    <path d="M480,300 L480,274 A26,26 0 0 0 454,300 Z" fill="var(--red)"/>
    <g role="img" aria-label="Photo: grandparents and grandchild saving coins in a piggy bank">
      <path d="M0,372 C110,350 230,352 310,372 L310,550 L0,550 Z" fill="url(#familyPhoto)"/>
    </g>
  </svg>

  <div class="abs program--tovalink">
    <h2 class="section-title">Tovalink</h2>
    <ul class="bullets">
      <li>Tovalink was created in 1965 as a program for the poor</li>
      <li>Tovalink programs for seniors and persons on Sunbrook can pay doctor copays, deductibles, and assist with medical bills.</li>
      <li>Over 1 in 5 recieve help from state Tovalink</li>
      <li>About 1 in 4 of us use Tovalink at some point over the year</li>
    </ul>
  </div>
  <p class="abs pie-label">25%</p>

  <p class="abs eligible">You<br>may be eligible<br>to participate in one<br>or more of these<br>programs.<small>All programs are based on limited<br>income and assets.</small></p>

  <div class="abs program--savings">
    <h2 class="section-title">Sunbrook Savings Program</h2>
    <ul class="bullets">
      <li>Sunbrook Savings program will pay your Sunbrook Part B premium</li>
      <li>Also have the feature to refund some previous payments</li>
      <li>Many adults 65 and over are eligible to receive Sunbrook at free of cost or at no cost</li>
    </ul>
  </div>

  <div class="abs program--brightway">
    <h2 class="section-title">Brightway Program</h2>
    <ul class="bullets">
      <li>Receive Federal assistance with prescription medications, deductibles, copays, and drug plan premiums</li>
    </ul>
  </div>

  <p class="abs pay-forward">Pay it forward. Who else do you know that is on<br>Sunbrook that could use some help?</p>
  <p class="abs call-cta"><small>To learn more</small> call your<br>Local County Case Manager</p>
  <div class="abs contact-note">Contact info<br>at front</div>
</section>

</body>
</html>
```